KRV Affirmation and Intention Card Design

I would like to have designs created that will be used on my Affirmation and Intention Cards I will be selling. We are a luxury brand. The designs need to be aesthetically pleasing, but minimal (think blush pinks/matte blacks/cream/warm earth tones/teals with gold/rose gold/silver lettering and visuals. Intention cards will have the same intentions as the inspiration photo. Affirmation cards will have random inspirational and biblical quotes. I only need two designs for the back of the Affirmation cards. One for design for every day quotes and one design for biblical quotes. For the intentions cards I would like a design for one side of card that will be on all cards and on the other side a design that correlates with each intention. See inspiration photo attached.

Target Market(s)

Millennials/ Women/ Similiar to Inspiration Photos below. Design that will look well on any color card stock I choose.

Industry/Entity Type

Lifestyle

Requirements
Must have
• Design that can fit on cards approximately 4 x 2.5 or 4x3 or 3.5 x 2.5 in size

```html
<!DOCTYPE html>
<html lang="en">
<head>
<meta charset="UTF-8">
<title>Affirmation Cards</title>
<link rel="stylesheet" href="https://fonts.googleapis.com/css2?family=Poppins:ital,wght@0,400;1,500&display=swap">
<style>
  :root {
    --teal: #07605e;
    --gold: #9c7a3c;
    --gold-soft: #b08e4e;
    --ink: #333333;
    --paper: #ffffff;
  }
  * { margin: 0; padding: 0; box-sizing: border-box; }
  html, body {
    width: 812px;
    height: 1200px;
    overflow: hidden;
    background: var(--paper);
  }
  .stage {
    position: relative;
    width: 812px;
    height: 1200px;
  }
  .card {
    position: absolute;
    top: 340px;
    width: 272px;
    height: 434px;
    background: var(--teal);
    overflow: hidden;
  }
  .card--faith { left: 109px; }
  .card--journey { left: 431px; }
  .card svg {
    position: absolute;
    inset: 0;
  }
  .card-quote {
    position: absolute;
    left: 0;
    right: 0;
    text-align: center;
    font-family: "Poppins", sans-serif;
    font-style: italic;
    font-weight: 500;
    color: var(--gold);
    text-transform: uppercase;
  }
  .card--faith .card-quote {
    top: 102px;
    font-size: 23px;
    line-height: 31.5px;
  }
  .card--journey .card-quote {
    top: 131px;
    font-size: 25.5px;
    line-height: 35.5px;
    letter-spacing: 0.3px;
  }
  .size-label {
    position: absolute;
    top: 814px;
    left: 0;
    right: 0;
    text-align: center;
    font-family: "Poppins", sans-serif;
    font-weight: 400;
    font-size: 41px;
    color: var(--ink);
  }
</style>
</head>
<body>
<main class="stage">

  <section class="card card--faith">
    <svg width="272" height="434" viewBox="0 0 272 434">
      <defs>
        <linearGradient id="figureTone" x1="0" y1="0" x2="0" y2="1">
          <stop offset="0" stop-color="#9c7a3c"/>
          <stop offset="1" stop-color="#b08e4e"/>
        </linearGradient>
      </defs>
      <circle class="wreath" role="img" aria-label="Floral wreath ornament framing the quote"
              cx="136" cy="164" r="112" fill="none" stroke="var(--gold)" stroke-width="20"/>
      <circle class="accent-dot" cx="136" cy="303" r="6" fill="var(--gold)"/>
      <g class="figure" role="img" aria-label="Silhouette of a seated woman on a round base">
        <rect x="100" y="313" width="72" height="104" rx="30" fill="url(#figureTone)"/>
        <ellipse cx="136" cy="419" rx="88" ry="13" fill="url(#figureTone)"/>
      </g>
    </svg>
    <p class="card-quote">I live<br>by baith,<br>not<br>by sight</p>
  </section>

  <section class="card card--journey">
    <svg width="272" height="434" viewBox="0 0 272 434">
      <rect class="border-band" role="img" aria-label="Ornamental lace border pattern"
            x="0" y="8" width="272" height="47" fill="var(--gold)"/>
      <rect class="rule" x="0" y="60" width="272" height="5" fill="var(--gold)"/>
      <path class="mandala" role="img" aria-label="Half mandala ornament"
            d="M6 434 A130 130 0 0 1 266 434 Z" fill="var(--gold)"/>
    </svg>
    <p class="card-quote">Each journey<br>is a work<br>of art</p>
  </section>

  <p class="size-label">2.5 X 4.0</p>

</main>
</body>
</html>
```